Business card design needed

My company specialises in carpentry and building services.
Based in Brisbane QLD
We also do:
property maintenance
plastering
painting
tiling
property maintenance

Industry/Entity Type

Carpentry

Contact Information for Business Card

RT Services QLD
Mark 0412583047
Dean 0493217586

```html
<!DOCTYPE html>
<html lang="en">
<head>
<meta charset="utf-8">
<title>RT Services QLD — Business Card</title>
<link rel="stylesheet" href="https://fonts.googleapis.com/css2?family=Open+Sans:wght@400&family=Playfair+Display:wght@400&display=swap">
<style>
  :root {
    --bg-light: #f4f4f4;
    --bg-mid: #d9d9d9;
    --card-dark: #0b0b0b;
    --card-mid: #1d1d1d;
    --text-silver: #c9c9c9;
    --text-bright: #e6e6e6;
    --divider: rgba(255, 255, 255, 0.09);
    --shadow: rgba(0, 0, 0, 0.35);
  }
  * { box-sizing: border-box; margin: 0; padding: 0; }
  html, body {
    width: 1200px;
    height: 896px;
    overflow: hidden;
  }
  body {
    background: radial-gradient(ellipse at 50% 40%, var(--bg-light) 0%, var(--bg-mid) 100%);
    position: relative;
    font-family: "Open Sans", Arial, sans-serif;
  }
  .card {
    position: absolute;
    width: 600px;
    height: 340px;
    background: linear-gradient(135deg, var(--card-mid) 0%, var(--card-dark) 70%);
    box-shadow: 0 14px 30px var(--shadow);
    overflow: hidden;
  }
  .card::before {
    content: "";
    position: absolute;
    top: 0;
    bottom: 0;
    left: 330px;
    width: 1px;
    background: var(--divider);
  }
  .card--front { left: 540px; top: 90px; }
  .card--back { left: 80px; top: 470px; }

  /* Front */
  .services {
    position: absolute;
    right: 282px;
    top: 110px;
    text-align: right;
    color: var(--text-silver);
  }
  .services__title {
    font-size: 17px;
    letter-spacing: -0.2px;
    margin-bottom: 4px;
  }
  .services__list {
    list-style: none;
    font-size: 11px;
    line-height: 14px;
  }
  .brand-name {
    position: absolute;
    left: 348px;
    top: 140px;
    font-family: "Playfair Display", Georgia, serif;
    font-size: 28px;
    line-height: 34px;
    color: var(--text-bright);
  }

  /* Back */
  .contact {
    position: absolute;
    top: 120px;
    left: 0;
    right: 0;
  }
  .contact__row {
    position: relative;
    height: 48px;
  }
  .contact__phone {
    position: absolute;
    right: 282px;
    top: 4px;
    display: flex;
    align-items: center;
    gap: 12px;
    font-size: 12px;
    color: var(--text-silver);
  }
  .contact__icon { width: 16px; height: 13px; fill: var(--text-silver); }
  .contact__name {
    position: absolute;
    left: 350px;
    top: 0;
    font-family: "Playfair Display", Georgia, serif;
    font-size: 24px;
    color: var(--text-bright);
  }
</style>
</head>
<body>

<section class="card card--front" aria-label="Business card front">
  <div class="services">
    <p class="services__title">Carpentry &amp; Building Services</p>
    <ul class="services__list">
      <li>Property Maintenance</li>
      <li>Plastering</li>
      <li>Painting</li>
      <li>Tiling</li>
    </ul>
  </div>
  <p class="brand-name">RT Services<br>QLD</p>
</section>

<section class="card card--back" aria-label="Business card back">
  <svg width="0" height="0" style="position:absolute">
    <symbol id="icon-phone" viewBox="0 0 16 13">
      <path d="M1 4 C1 1.5 4 0.5 8 0.5 C12 0.5 15 1.5 15 4 L15 5 L11.5 5 L11.5 3.5 L4.5 3.5 L4.5 5 L1 5 Z"/>
      <path d="M3 6 L5 6 L5.5 5 L10.5 5 L11 6 L13 6 L14 12.5 L2 12.5 Z"/>
    </symbol>
  </svg>
  <div class="contact">
    <div class="contact__row">
      <p class="contact__phone">0412583047
        <svg class="contact__icon" aria-hidden="true"><use href="#icon-phone"/></svg>
      </p>
      <p class="contact__name">Mark</p>
    </div>
    <div class="contact__row">
      <p class="contact__phone">0493217586
        <svg class="contact__icon" aria-hidden="true"><use href="#icon-phone"/></svg>
      </p>
      <p class="contact__name">Dean</p>
    </div>
  </div>
</section>

</body>
</html>
```